The Copper Fellow Mo Wax Label

Hi Chaps,

We are needing a lable for our new moustache wax.

The design needs to be on a circular label. the size of the label is 32mm in diameter.

It needs to align with our branding from our beard oil product. checkout www.thecopperfellow-demo.com to get an insight of this.

what needs to be on the label:

- The copper fellow logo (please pull from website, will send through hi def image when design is selected)
- Fine Grain Moustache Wax
- the word "soft/medium hold"

This project will be open for 48 hours.

Any questions, please ask asap.
Updates

Our Logo and fonts that we use for our brand are now attached to the brief. 

Industry/Entity Type

Product

Requirements
Must have
• Must have
The copper fellow logo (please pull from website, will send through hi def image when design is selected)
- Fine Grain Moustache Wax
- allign with branding
- actual size 32mm diameter

```html
<!DOCTYPE html>
<html lang="en">
<head>
<meta charset="utf-8">
<title>Fine Grain Moustache Wax — Label</title>
<link href="https://fonts.googleapis.com/css2?family=Bebas+Neue&family=Playfair+Display:ital@1&display=swap" rel="stylesheet">
<style>
  :root {
    --bg-top: #161616;
    --bg-bottom: #5c5c5c;
    --label: #f2f2f2;
    --ink: #0a0a0a;
    --shadow: rgba(0, 0, 0, 0.45);
  }
  html, body {
    margin: 0;
    padding: 0;
    width: 1200px;
    height: 900px;
    overflow: hidden;
  }
  .canvas {
    position: relative;
    width: 1200px;
    height: 900px;
    background: linear-gradient(to bottom, var(--bg-top), var(--bg-bottom));
    overflow: hidden;
  }
  .label-shadow {
    position: absolute;
    left: 270px;
    top: 832px;
    width: 660px;
    height: 26px;
    border-radius: 50%;
    background: var(--shadow);
    filter: blur(10px);
  }
  .label {
    position: absolute;
    left: 249px;
    top: 108px;
    width: 702px;
    height: 702px;
    border-radius: 50%;
    background: var(--label);
  }
  .product-name {
    position: absolute;
    left: 0;
    right: 0;
    top: 78px;
    margin: 0;
    text-align: center;
    font-family: "Bebas Neue", "Oswald", sans-serif;
    font-weight: 400;
    font-size: 92px;
    line-height: 84px;
    letter-spacing: 1px;
    color: var(--ink);
  }
  .hold-strength {
    position: absolute;
    left: 0;
    right: 0;
    top: 252px;
    margin: 0;
    text-align: center;
    font-family: "Playfair Display", Georgia, serif;
    font-style: italic;
    font-size: 40px;
    letter-spacing: 1px;
    color: var(--ink);
  }
  .moustache-art {
    position: absolute;
    left: 66px;
    top: 316px;
    width: 578px;
    height: 170px;
    border-radius: 85px;
    background: var(--ink);
  }
  .brand-mark {
    position: absolute;
    left: 0;
    right: 0;
    top: 528px;
    margin: 0;
    text-align: center;
    font-family: "Bebas Neue", "Oswald", sans-serif;
    font-size: 40px;
    line-height: 40px;
    color: var(--ink);
  }
</style>
</head>
<body>
  <div class="canvas">
    <div class="label-shadow"></div>
    <div class="label">
      <h1 class="product-name">Fine Grain<br>Moustache Wax</h1>
      <p class="hold-strength">Soft/medium hold</p>
      <div class="moustache-art" role="img" aria-label="Black curled handlebar moustache silhouette"></div>
      <p class="brand-mark">The Copper Fellow</p>
    </div>
  </div>
</body>
</html>
```